Kalvendor Whitmane & Associates

We would like a simple, professional business card using a similar font to our logo.

Industry/Entity Type

Law Firm

Contact Information for Business Card

Martin Kalvendor, Esq. 48 Fennimore Lane, 2nd Floor Ollerbrook, NH 04173 Office: 555.216.4093 Cell: 555.370.8154 Email: marty@kwlawfirm.example kalvendorwhitmanelaw.example

Font styles to use
Other font styles liked:
• We would like to use the fonts used in the logo or similar

Colors
0054AA
0677BA
7BADD7
CADEEF
E8F1F8

Requirements
Must have
• We would like the fonts to match the logo
Nice to have
• not too much design- very simple and professional business card. I added a picture of a business card that I tried to start but I am not a designer! Hopefully it will help with the address and phone numbers and kind of what we are looking for.

```html
<!DOCTYPE html>
<html lang="en">
<head>
<meta charset="utf-8">
<title>Kalvendor Whitmane &amp; Associates – Business Card</title>
<link rel="stylesheet" href="https://fonts.googleapis.com/css2?family=Cinzel:wght@400;600&display=swap">
<style>
  :root {
    --navy: #233c7a;
    --navy-deep: #1c3169;
    --paper: #f7f8fa;
    --backdrop: #d9dde4;
    --rule-grey: #7a7f88;
    --white: #ffffff;
  }
  * { margin: 0; padding: 0; box-sizing: border-box; }
  html, body { width: 1200px; height: 675px; overflow: hidden; }
  body {
    background: var(--backdrop);
    font-family: "Cinzel", "Times New Roman", serif;
    position: relative;
  }
  .card {
    position: absolute;
    top: 195px;
    width: 500px;
    height: 286px;
    box-shadow: 0 10px 24px rgba(30, 40, 60, 0.18);
  }
  .card--front { left: 60px; background: var(--paper); color: var(--navy); }
  .card--back  { left: 640px; background: linear-gradient(160deg, #2d4a8a, var(--navy-deep)); color: var(--white); }

  .brand {
    position: absolute;
    display: flex;
    align-items: center;
  }
  .brand__square { flex: none; }
  .brand__divider { width: 2px; align-self: stretch; }
  .brand__name {
    font-weight: 600;
    text-transform: uppercase;
    line-height: 1;
  }

  .card--front .brand { left: 120px; top: 34px; gap: 12px; height: 62px; }
  .card--front .brand__square { width: 62px; height: 44px; background: var(--navy); }
  .card--front .brand__divider { background: var(--rule-grey); }
  .card--front .brand__name { font-size: 15px; color: var(--navy); }

  .front__rule {
    position: absolute;
    left: 40px;
    width: 420px;
    height: 1.5px;
    background: var(--navy);
  }
  .front__rule--top { top: 116px; left: 200px; width: 260px; }
  .front__rule--mid { top: 192px; }

  .front__person {
    position: absolute;
    top: 132px; left: 0; width: 100%;
    text-align: center;
    font-size: 21px;
    font-weight: 600;
    letter-spacing: 0.5px;
  }
  .front__line {
    position: absolute;
    left: 0; width: 100%;
    text-align: center;
    font-size: 11.5px;
    letter-spacing: 0.4px;
    white-space: nowrap;
  }
  .front__address { top: 170px; }
  .front__phones  { top: 206px; }
  .front__web     { top: 230px; }

  .card--back .brand { left: 86px; top: 78px; gap: 14px; height: 92px; }
  .card--back .brand__square { width: 100px; height: 66px; background: var(--white); }
  .card--back .brand__divider { background: var(--white); }
  .card--back .brand__name { font-size: 21px; color: var(--white); }

  .back__url {
    position: absolute;
    top: 222px; left: 0; width: 100%;
    text-align: center;
    font-size: 12.5px;
    letter-spacing: 2.5px;
    white-space: nowrap;
  }
</style>
</head>
<body>
  <section class="card card--front" aria-label="Card front">
    <div class="brand">
      <span class="brand__square"></span>
      <span class="brand__divider"></span>
      <span class="brand__name">Kalvendor<br>Whitmane<br>&amp; Associates</span>
    </div>
    <div class="front__rule front__rule--top"></div>
    <p class="front__person">Martin Kalvendor, Esq.</p>
    <p class="front__line front__address">48 Fennimore Lane, 2nd Floor, Ollerbrook, NH 04173</p>
    <div class="front__rule front__rule--mid"></div>
    <p class="front__line front__phones">Office (555.216.4093) | Phone (555.370.8154)</p>
    <p class="front__line front__web">marty@kwlawfirm.example | kalvendorwhitmanelaw.example</p>
  </section>

  <section class="card card--back" aria-label="Card back">
    <div class="brand">
      <span class="brand__square"></span>
      <span class="brand__divider"></span>
      <span class="brand__name">Kalvendor<br>Whitmane<br>&amp; Associates</span>
    </div>
    <p class="back__url">www.kalvendorwhitmanelaw.example</p>
  </section>
</body>
</html>
```